Website Design: Neuroscience research lab at an academic University.

I am looking to redo my University website for Neuroscience Research. <br/><br/>I am looking for a clean, modern and organized design to publish our work. Although I want a modern look, the focus should be on the text content.<br/><br/>Pages I need. These pages should be in the navigation bar;<br/>*Home*: with overview of the lab, contact information, and possibly with <br/>"Recent News and Events" information<br/>*Research*/Projects: will have text description, images, as well as video of various research projects we have done or are working on<br/>*People*: Personnel page with photos and bios of the team<br/>*Publications*: List of research articles with hyperlinks to online <br/>versions of articles as well as PDFs<br/>*News*: Continually updated list of events<br/><br/><br/>Some designs I like: <br/><br/>https://www.moravinlabs.example/<br/>http://www.quillbranch.example/<br/>https://tovernilab.example<br/>http://www.gradmerlab.example/<br/>https://vkot.halvern.example/

Target Market(s)

Academics, university students, government

Logo Text

Morvek Lab

Number of Pages Required

5+ page

Colors

Designer to choose colors to be used in the design.

Requirements
Must have
• A modern but elegant design that focuses on the research but that is also visually appealing.
• For the logo, please see the sketch in the attached files. That is a rough sketch of a logo that you can base your logo design on.
Should not have
• No search bar

```html
<!DOCTYPE html>
<html lang="en">
<head>
<meta charset="utf-8">
<title>Morvek Lab – Neuroscience Research</title>
<link href="https://fonts.googleapis.com/css2?family=Montserrat:wght@500;600;700&family=Lato:wght@400;700&display=swap" rel="stylesheet">
<style>
:root{
  --blue:#2546b8;
  --blue-dark:#1f3a9e;
  --green:#4b9a2a;
  --purple:#7a2fd2;
  --magenta:#a0267a;
  --navy:#0c1c3c;
  --ink:#111;
  --text:#444;
  --red:#d8262d;
  --field:#ececec;
  --footer:#141414;
}
*{margin:0;padding:0;box-sizing:border-box}
html,body{width:1200px;height:3968px;overflow:hidden}
body{font-family:"Lato",sans-serif;color:var(--text);background:#fff;position:relative}
h1,h2,h3,h4{font-family:"Montserrat",sans-serif;font-weight:600}
section,header,footer{position:absolute;left:0;width:1200px}
ul{list-style:none}
.bullets li{position:relative;padding-left:36px}
.bullets li::before{content:"";position:absolute;left:0;top:.6em;width:9px;height:9px;border-radius:50%;background:currentColor}

/* header */
.site-header{top:0;height:83px;background:#fff}
.brand{position:absolute;left:90px;top:20px;display:flex;align-items:center;gap:10px;font-family:"Montserrat",sans-serif;font-weight:600;font-size:20px;color:var(--ink)}
.brand-dot{width:36px;height:36px;border-radius:50%;background:var(--blue)}
.main-nav{position:absolute;right:92px;top:31px;display:flex;gap:36px;font-family:"Lato",sans-serif;font-weight:700;font-size:16px;color:#222}
.main-nav .active{color:var(--red)}

/* hero */
.hero{top:83px;height:549px;background:radial-gradient(ellipse at 55% 45%,#c2452a 0%,#6b1d3a 40%,#1a0d2a 80%)}
.hero-title{position:absolute;top:150px;width:100%;text-align:center;color:#fff;font-size:50px;line-height:56px}
.hero-btn{position:absolute;left:508px;top:314px;width:184px;height:56px;border-radius:28px;background:var(--blue);color:#fff;font-family:"Montserrat",sans-serif;font-weight:600;font-size:17px;display:flex;align-items:center;justify-content:center}
.hero-dots{position:absolute;top:498px;left:550px;display:flex;gap:13px}
.hero-dots span{width:14px;height:14px;border-radius:50%;border:2px solid #fff}
.hero-dots span.on{background:var(--blue);border-color:var(--blue)}

/* welcome */
.welcome{top:632px;height:632px}
.section-title{position:absolute;width:100%;text-align:center;font-size:43px;color:var(--ink)}
.section-title em{font-style:normal;color:var(--blue)}
.rule{position:absolute;height:3px;width:40px;background:var(--blue)}
.welcome .section-title{top:76px}
.welcome .rule{left:580px;top:141px}
.feature-box{position:absolute;top:189px;width:402px;height:342px;color:#fff;padding:42px 44px}
.feature-box h3{font-size:31px;margin-bottom:22px}
.feature-box li{font-size:17px;line-height:31px;margin-bottom:13px;padding-left:46px}
.feature-box li::before{left:12px}
.box-blue{left:155px;background:var(--blue)}
.box-green{left:637px;background:var(--green)}

/* about */
.about{top:1264px;height:549px;background:linear-gradient(90deg,#0d2a55 0%,#123a6a 40%,#0a1d3a 100%)}
.about-art{position:absolute;left:0;top:0;width:560px;height:549px;background:radial-gradient(ellipse at 60% 40%,#d24a6a 0%,#2e6aa0 35%,transparent 70%)}
.about-body{position:absolute;left:559px;top:82px;width:530px;color:#fff}
.about-body h2{font-size:42px}
.about-body .rule{position:static;margin:14px 0 22px;background:var(--green)}
.about-body li{font-size:15.5px;line-height:27px;padding-left:36px}
.outline-btn{display:inline-flex;margin-top:26px;width:150px;height:48px;border:1.5px solid #fff;border-radius:24px;align-items:center;justify-content:center;font-family:"Montserrat",sans-serif;font-weight:600;font-size:16px;color:#fff}

/* split */
.split{top:1813px;height:546px;display:flex}
.split-col{width:600px;height:546px;position:relative;padding:88px 40px 0 92px}
.split-neural{background:linear-gradient(135deg,#5a1a6a 0%,#8a2a8a 45%,#3a1460 100%);color:#fff}
.split-memory{background:#fff;padding-left:67px;padding-right:62px}
.split-col h2{font-size:40px;line-height:43px}
.split-col .rule{position:static;margin:16px 0 36px}
.split-neural .rule{background:#fff}
.split-col li{font-size:15.5px;line-height:27px}
.split-memory li{color:#333}
.split-memory li::before{color:var(--blue)}

/* news */
.news{top:2359px;height:695px;background:linear-gradient(180deg,#6a24c8 0%,#7a33dc 50%,#5a1cb0 100%)}
.news .section-title{top:126px;color:#fff}
.news-card{position:absolute;top:210px;width:327px;height:372px;background:#fff}
.news-img{height:173px}
.news-card:nth-of-type(1) .news-img{background:linear-gradient(135deg,#cfe0ee,#7aa6c8)}
.news-card:nth-of-type(2) .news-img{background:linear-gradient(135deg,#3a6ad0,#c84a5a)}
.news-card:nth-of-type(3) .news-img{background:linear-gradient(135deg,#eaeef2,#5a8ac8)}
.news-meta{padding:28px 24px 0;font-size:12px;color:var(--magenta);display:flex;align-items:center;gap:10px}
.news-meta svg{width:13px;height:13px}
.news-card h4{padding:8px 24px 0;font-size:18px;color:var(--ink)}
.news-card p{padding:16px 24px 0;font-size:13.5px;line-height:21px;color:#333;text-align:justify}
.read-more{display:block;padding:18px 24px 0;font-size:15px;color:var(--magenta)}

/* contact */
.contact{top:3054px;height:627px}
.contact .section-title{top:80px}
.contact .rule{left:580px;top:146px}
.field{position:absolute;background:var(--field);font-size:16px;color:#888;padding:12px 18px;height:48px}
.field.msg{height:128px}
.submit-btn{position:absolute;left:519px;top:485px;width:160px;height:49px;border-radius:25px;background:var(--blue);color:#fff;font-family:"Montserrat",sans-serif;font-weight:600;font-size:17px;display:flex;align-items:center;justify-content:center}

/* footer */
.site-footer{top:3681px;height:287px;background:var(--footer);color:#fff}
.foot-col{position:absolute;top:48px}
.foot-col h4{font-size:17px;font-weight:500;margin-bottom:16px}
.foot-small{font-size:11.5px;line-height:19px}
.foot-line{display:flex;align-items:center;gap:16px;font-size:15px;margin-top:14px}
.foot-line + .foot-line{font-size:12.5px;margin-top:6px}
.newsletter-form{display:flex;margin-top:22px;width:278px;height:41px;border:1px solid #fff}
.newsletter-form span{flex:1;background:#fff;color:#222;font-size:12px;padding:13px 12px}
.newsletter-form b{width:84px;background:var(--blue);font-weight:400;font-size:15px;display:flex;align-items:center;justify-content:center}
.quick-links{display:grid;grid-template-columns:164px 100px;font-size:11.5px;line-height:21px}
.social li{display:flex;align-items:center;gap:14px;font-size:12px;line-height:30px}
.social i{width:9px;height:9px;border-radius:50%;background:#fff}
.copyright{position:absolute;bottom:8px;width:100%;text-align:center;font-size:11px}
</style>
</head>
<body>

<header class="site-header">
  <div class="brand"><span class="brand-dot"></span>Morvek Lab</div>
  <nav class="main-nav">
    <span class="active">Home</span><span>Recent News and Events</span><span>Research</span><span>People</span><span>Publications</span><span>News</span><span>Contact</span>
  </nav>
</header>

<section class="hero" role="img" aria-label="Glowing network of orange neurons on a dark background">
  <h1 class="hero-title">Neuroscience Research lab at<br>an Academic university</h1>
  <a class="hero-btn">Learn More</a>
  <div class="hero-dots"><span class="on"></span><span></span><span></span><span></span></div>
</section>

<section class="welcome">
  <h2 class="section-title">Welcome to <em>Morvek Lab</em></h2>
  <div class="rule"></div>
  <div class="feature-box box-blue">
    <h3>What We Do</h3>
    <ul class="bullets">
      <li>Lorem ipsum dolor sit amet, consectetur adipiscing elit, sed do eiusmod tempor incididunt</li>
      <li>Lorem ipsum dolor sit amet, consectetur adipiscing elit, sed do eiusmod tempor incididunt</li>
    </ul>
  </div>
  <div class="feature-box box-green">
    <h3>Research</h3>
    <ul class="bullets">
      <li>Lorem ipsum dolor sit amet, consectetur adipiscing elit, sed do eiusmod tempor incididunt</li>
      <li>Lorem ipsum dolor sit amet, consectetur adipiscing elit, sed do eiusmod tempor incididunt</li>
    </ul>
  </div>
</section>

<section class="about">
  <div class="about-art" role="img" aria-label="Synapse with an electric spark between two neuron terminals"></div>
  <div class="about-body">
    <h2>About</h2>
    <div class="rule"></div>
    <ul class="bullets">
      <li>Lorem ipsum dolor sit amet, consectetur adipiscing elit, sed do eiusmod tempor incididunt ut labore et dolore magna aliqua.</li>
      <li>Lorem ipsum dolor sit amet, consectetur adipiscing elit, sed do eiusmod tempor incididunt ut labore et dolore magna aliqua.</li>
      <li>Lorem ipsum dolor sit amet, consectetur adipiscing elit, sed do eiusmod tempor incididunt ut labore et dolore magna aliqua.</li>
      <li>Lorem ipsum dolor sit amet, consectetur adipiscing elit, sed do eiusmod tempor incididunt ut labore et dolore magna aliqua.</li>
    </ul>
    <a class="outline-btn">Learn More</a>
  </div>
</section>

<section class="split">
  <div class="split-col split-neural" role="img" aria-label="Purple and magenta neuron imagery behind the text">
    <h2>Realtime Neural<br>Engineering</h2>
    <div class="rule"></div>
    <ul class="bullets">
      <li>Lorem ipsum dolor sit amet, consectetur adipiscing elit, sed do eiusmod tempor incididunt ut labore et dolore magna aliqua. Ut enim ad minim veniam, quis nostrud exercitation ullamco ris nisi ut aliquip ex ea commodo consequat.</li>
      <li>Duis aute Irure dolor in reprehenderit in voluptate velit esse cillum dolore eu fugiat nulla</li>
      <li>pariatur. Excepteur sint occaecat cupidatat non Proident, sunt in culpa qui officia deserunt mollit anim id est laborum</li>
    </ul>
  </div>
  <div class="split-col split-memory">
    <h2>Interacting with<br>Memory</h2>
    <div class="rule"></div>
    <ul class="bullets">
      <li>Lorem ipsum dolor sit amet, consectetur adipiscing elit, sed do eiusmod tempor incididunt ut labore et dolore magna aliqua. Ut enim ad minim veniam, quis nostrud exercitation ullamco ris nisi ut aliquip ex ea commodo consequat.</li>
      <li>Duis aute Irure dolor in reprehenderit in voluptate velit esse cillum dolore eu fugiat nulla</li>
      <li>pariatur. Excepteur sint occaecat cupidatat non Proident, sunt in culpa qui officia deserunt mollit anim id est laborum</li>
    </ul>
  </div>
</section>

<section class="news" role="img" aria-label="Violet background of glowing neuron networks">
  <h2 class="section-title">Latest News</h2>
  <article class="news-card" style="left:86px">
    <div class="news-img" role="img" aria-label="Lab researcher handling samples"></div>
    <div class="news-meta"><svg viewBox="0 0 13 13"><rect x="1" y="2" width="11" height="10" fill="none" stroke="currentColor"/><rect x="1" y="2" width="11" height="3" fill="currentColor"/></svg>APR 18th, 2019</div>
    <h4>Lorem ipsum dolor sit amet</h4>
    <p>Duis aute irure dolor in reprehenderit in voluptate velit esse cillum dolore eu fugiat</p>
    <a class="read-more">READ MORE</a>
  </article>
  <article class="news-card" style="left:434px">
    <div class="news-img" role="img" aria-label="Neuron cell above test tubes"></div>
    <div class="news-meta"><svg viewBox="0 0 13 13"><rect x="1" y="2" width="11" height="10" fill="none" stroke="currentColor"/><rect x="1" y="2" width="11" height="3" fill="currentColor"/></svg>APR 18th, 2019</div>
    <h4>Lorem ipsum dolor sit amet</h4>
    <p>Duis aute irure dolor in reprehenderit in voluptate velit esse cillum dolore eu fugiat</p>
    <a class="read-more">READ MORE</a>
  </article>
  <article class="news-card" style="left:782px">
    <div class="news-img" role="img" aria-label="Researcher in protective gear holding a lab mouse"></div>
    <div class="news-meta"><svg viewBox="0 0 13 13"><rect x="1" y="2" width="11" height="10" fill="none" stroke="currentColor"/><rect x="1" y="2" width="11" height="3" fill="currentColor"/></svg>APR 18th, 2019</div>
    <h4>Lorem ipsum dolor sit amet</h4>
    <p>Duis aute irure dolor in reprehenderit in voluptate velit esse cillum dolore eu fugiat</p>
    <a class="read-more">READ MORE</a>
  </article>
</section>

<section class="contact">
  <h2 class="section-title">Contact <em>Us</em></h2>
  <div class="rule"></div>
  <div class="field" style="left:126px;top:192px;width:456px">Name*</div>
  <div class="field" style="left:619px;top:192px;width:454px">E-mail*</div>
  <div class="field" style="left:126px;top:263px;width:456px">Title</div>
  <div class="field" style="left:619px;top:263px;width:454px">Organization</div>
  <div class="field msg" style="left:126px;top:332px;width:947px">Message</div>
  <a class="submit-btn">SUBMIT</a>
</section>

<footer class="site-footer">
  <div class="foot-col" style="left:91px">
    <h4>CONTACT US</h4>
    <p class="foot-small">2214 Larkfield Research Way,<br>Dunmore, OH 44102 USA</p>
    <div class="foot-line" style="margin-top:18px"><svg width="18" height="18" viewBox="0 0 18 18"><path d="M4 2l3 3-2 2c1 2 3 4 5 5l2-2 3 3-2 2C8 15 3 10 2 4z" fill="none" stroke="#fff"/></svg>+1 555 0148 2290</div>
    <div class="foot-line"><svg width="18" height="14" viewBox="0 0 18 14"><rect x="1" y="1" width="16" height="12" fill="none" stroke="#fff"/><path d="M1 1l8 7 8-7" fill="none" stroke="#fff"/></svg>hello@morveklab.example</div>
  </div>
  <div class="foot-col" style="left:354px">
    <h4>NEWSLETTER</h4>
    <p class="foot-small" style="width:280px">Excepteur sint occaecat cupidatat non proident, sunt in culpa qui officia deserunt mollit anim</p>
    <div class="newsletter-form"><span>Enter your email address</span><b>Sign Up</b></div>
  </div>
  <div class="foot-col" style="left:713px">
    <h4>QUICK LINKS</h4>
    <div class="quick-links">
      <span>Home</span><span>Publications</span>
      <span>Recent News and Events</span><span>News</span>
      <span>Research</span><span>Contact</span>
      <span>People</span>
    </div>
  </div>
  <div class="foot-col" style="left:1010px">
    <h4>SOCIAL MEDIA</h4>
    <ul class="social">
      <li><i></i>Friendline</li>
      <li><i></i>Chirpnet</li>
      <li><i></i>Circlepost</li>
      <li><i></i>Clipstream</li>
    </ul>
  </div>
  <p class="copyright">© 2019 The Company Name.All Rights Reserved</p>
</footer>

</body>
</html>
```